Post it Note design

POST-IT NOTE DESIGN (CONTENT)
Size recommended: 4x6 for handwriting space.
Header (Bold):
Lighting Issue Detected on Your Property
Sub-header:
During our routine night inspection, we noted the following item(s):
Checkbox List:
⬜ Building Lights Out
⬜ Pole Lights Out
⬜ Sign Not Illuminated
⬜ Other ________________________
Action Line:
We can provide a quote or dispatch service right away.
Area for notes
Contact Block (Bold & Centered):
Brovane Fixture Inc.
Service@BrovaneFixture.com
www.BrovaneFixture.com
877-514-0862
Industry/Entity Type
Electrical lighting
Colors
Designer to choose colors to be used in the design.
Look and feel
Each slider illustrates characteristics of the customer's brand and the style your logo design should communicate.

```html
<!DOCTYPE html>
<html lang="en">
<head>
<meta charset="utf-8">
<title>Brovane Fixture Inc. – Lighting Issue Note</title>
<link rel="stylesheet" href="https://fonts.googleapis.com/css2?family=Montserrat:wght@500;600;700;800;900&display=swap">
<style>
  :root {
    --brand-blue: #2b3990;
    --brand-red: #ed1c24;
    --ink: #111111;
    --paper: #ffffff;
    --rule: #d9d9d9;
    --backdrop: #ececec;
    --photo-light: #f2f2f2;
    --photo-mid: #c9ccd4;
  }
  * { box-sizing: border-box; margin: 0; padding: 0; }
  html, body {
    width: 696px; height: 1200px; overflow: hidden;
    background: var(--backdrop);
    font-family: "Montserrat", Arial, sans-serif;
  }
  .note {
    position: absolute; left: 18px; top: 105px;
    width: 660px; height: 990px;
    background: var(--paper);
    box-shadow: 0 6px 14px rgba(0,0,0,.25);
    overflow: hidden;
  }
  .hero-band {
    position: absolute; left: 0; top: 127px; width: 100%; height: 213px;
    background: var(--brand-blue);
  }
  .hero-photo {
    position: absolute; left: 88px; top: 16px; width: 500px; height: 300px;
    background: linear-gradient(180deg, var(--photo-light) 0%, var(--photo-mid) 100%);
    border-radius: 10px;
  }
  .brand-name {
    position: absolute; left: 0; top: 322px; width: 100%;
    text-align: center; color: var(--brand-red);
    font-weight: 900; font-size: 38px; line-height: 42px;
    text-transform: uppercase; letter-spacing: .5px;
  }
  .brand-sub {
    position: absolute; left: 0; top: 368px; width: 100%;
    text-align: center; color: var(--brand-red);
    font-weight: 900; font-size: 20px; text-transform: uppercase;
    letter-spacing: 1px;
  }
  .headline {
    position: absolute; left: 0; top: 414px; width: 100%;
    text-align: center; color: var(--brand-blue);
    font-weight: 900; font-size: 39px; line-height: 37px;
    text-transform: uppercase;
  }
  .subhead {
    position: absolute; left: 0; top: 520px; width: 100%;
    text-align: center; color: var(--ink);
    font-weight: 700; font-size: 18px; line-height: 24px;
    text-transform: uppercase;
  }
  .checklist {
    position: absolute; top: 597px; list-style: none;
    color: var(--brand-blue); font-weight: 600; font-size: 20px; line-height: 31px;
  }
  .checklist--left { left: 64px; }
  .checklist--right { left: 364px; top: 600px; }
  .checklist li { display: flex; align-items: center; }
  .checkbox {
    width: 18px; height: 18px; border: 1.5px solid #333; margin-right: 18px; flex: none;
  }
  .fill-line {
    display: inline-block; width: 150px; border-bottom: 1.5px solid var(--brand-blue);
    margin-left: 6px; height: 18px;
  }
  .action-line {
    position: absolute; left: 0; top: 690px; width: 100%;
    text-align: center; color: var(--ink); font-weight: 800; text-transform: uppercase;
  }
  .action-line .lead { font-size: 17px; line-height: 20px; display: block; }
  .action-line .main { font-size: 21px; line-height: 24px; display: block; }
  .notes-area .rule {
    position: absolute; left: 0; width: 100%; height: 0;
    border-top: 1.5px solid var(--rule);
  }
  .contact-label {
    position: absolute; left: 0; top: 855px; width: 100%;
    text-align: center; color: var(--brand-blue);
    font-weight: 800; font-size: 19px; text-transform: uppercase;
  }
  .contact-block {
    position: absolute; left: 0; top: 878px; width: 100%; height: 112px;
    background: var(--brand-red); text-align: center; color: var(--paper);
    padding-top: 2px;
  }
  .contact-block .company {
    color: var(--ink); font-weight: 800; font-size: 27px; line-height: 30px;
    text-transform: uppercase;
  }
  .contact-block .detail { font-weight: 600; font-size: 20px; line-height: 22px; }
  .contact-block .phone { font-weight: 800; font-size: 20px; line-height: 26px; }
</style>
</head>
<body>
  <article class="note">
    <div class="hero-band"></div>
    <div class="hero-photo" role="img" aria-label="Photo of a white bucket service truck with traffic cones"></div>
    <div class="brand-name">Brovane Fixture</div>
    <div class="brand-sub">Incorporated</div>

    <h1 class="headline">Lighting Issue Detected<br>On Your Property</h1>
    <p class="subhead">During our routine night inspection,<br>we noted the following item(s):</p>

    <ul class="checklist checklist--left">
      <li><span class="checkbox"></span>Building Lights Out</li>
      <li><span class="checkbox"></span>Pole Lights Out</li>
    </ul>
    <ul class="checklist checklist--right">
      <li><span class="checkbox"></span>Sign Not Illuminated</li>
      <li><span class="checkbox"></span>Other<span class="fill-line"></span></li>
    </ul>

    <p class="action-line">
      <span class="lead">We can provide a quote</span>
      <span class="main">or dispatch service right away.</span>
    </p>

    <div class="notes-area">
      <div class="rule" style="top:742px"></div>
      <div class="rule" style="top:788px"></div>
      <div class="rule" style="top:834px"></div>
    </div>

    <p class="contact-label">Contact Block</p>
    <footer class="contact-block">
      <p class="company">Brovane Fixture Inc.</p>
      <p class="detail">Service@BrovaneFixture.com</p>
      <p class="detail">www.BrovaneFixture.com</p>
      <p class="phone">877-514-0862</p>
    </footer>
  </article>
</body>
</html>
```